Supplement Label Design - Sports Nutrition

Design a sports nutrition/weight loss supplement label that stands out in a crowded space. Supplement bottle size is 200c and label size is 7" x 2.5" approximately. We're looking for a design that emphasizes the products name called VYK. Vyk is an abbreviation for Vigor, Yield & Kinetics. We want VYK to be the center/focus point of the bottle and have a memorable design to it.

Target Market(s)

Men & Women over 18

Industry/Entity Type

Supplement

Font styles to use
Sans Serif
Decorative

Requirements
Must have
• Emphasis on the product name VYK. Serious, Inspirational & Motivational feel to the design, typo & colors. Electrocution/lightning feel to the text. Right hand side of label is our formulation. Left hand side is dedicated to explaining the trifecta formulation idea.
Nice to have
• For example, we like the graphic design of "Drum" energy drinks because you can identify the bottle from a distance and is memorable. We think that less is more and we'd like the design/colors do most of the talking.
Should not have
• Cartroon/animated style.

```html
<!DOCTYPE html>
<html lang="en">
<head>
<meta charset="UTF-8">
<title>VYK Supplement Label</title>
<link rel="stylesheet" href="https://fonts.googleapis.com/css2?family=Montserrat:ital,wght@0,600;0,700;0,800;0,900;1,800&family=Roboto+Condensed:wght@400;700&display=swap">
<style>
  :root {
    --page-bg: #ffffff;
    --label-blue: #1e6fe8;
    --label-mid: #0b2f86;
    --label-black: #000000;
    --logo-ice: #e4f9ff;
    --accent-cyan: #37d3f2;
    --text-white: #ffffff;
    --panel-line: #ffffff;
    --panel-bg: #000000;
  }
  * { margin: 0; padding: 0; box-sizing: border-box; }
  html, body {
    width: 1200px;
    height: 785px;
    overflow: hidden;
    background: var(--page-bg);
  }
  .canvas {
    position: relative;
    width: 1200px;
    height: 785px;
  }
  .label {
    position: absolute;
    left: 50px;
    top: 196px;
    width: 1100px;
    height: 393px;
    overflow: hidden;
    background: linear-gradient(180deg, var(--label-blue) 0%, var(--label-mid) 38%, #030a1e 62%, var(--label-black) 80%);
  }
  .storm-backdrop {
    position: absolute;
    inset: 0;
    background:
      radial-gradient(ellipse 220px 120px at 510px 150px, rgba(190, 220, 255, 0.35), transparent 70%),
      radial-gradient(ellipse 160px 200px at 20px 120px, rgba(170, 200, 255, 0.18), transparent 70%),
      radial-gradient(ellipse 140px 200px at 1080px 120px, rgba(170, 200, 255, 0.18), transparent 70%);
  }
  .brand {
    position: absolute;
    left: 340px;
    top: 112px;
    width: 340px;
    text-align: center;
  }
  .brand-name {
    font-family: "Montserrat", sans-serif;
    font-weight: 900;
    font-size: 104px;
    line-height: 1;
    letter-spacing: 4px;
    color: var(--logo-ice);
  }
  .brand-tagline {
    margin-top: 14px;
    font-family: "Montserrat", sans-serif;
    font-weight: 800;
    font-style: italic;
    font-size: 15px;
    letter-spacing: 0.3px;
    color: var(--accent-cyan);
    text-transform: uppercase;
  }
  .content-box {
    position: absolute;
    left: 419px;
    top: 321px;
    width: 176px;
    height: 40px;
    border: 2px solid var(--text-white);
    text-align: center;
    font-family: "Montserrat", sans-serif;
    font-weight: 800;
    font-size: 13px;
    line-height: 16px;
    padding-top: 2px;
  }
  .content-type { color: var(--text-white); }
  .content-count { color: var(--accent-cyan); }
  .facts-panel {
    position: absolute;
    left: 780px;
    top: 62px;
    width: 278px;
    height: 214px;
    background: var(--panel-bg);
    border: 1.5px solid var(--panel-line);
    padding: 3px 5px;
    font-family: "Roboto Condensed", sans-serif;
    font-size: 6.6px;
    line-height: 8.4px;
    color: var(--text-white);
  }
  .facts-title {
    font-weight: 700;
    font-size: 10px;
    line-height: 12px;
    border-bottom: 1px solid var(--panel-line);
  }
  .facts-row {
    display: flex;
    justify-content: space-between;
    border-bottom: 0.5px solid rgba(255,255,255,0.6);
  }
  .facts-row.heavy { border-bottom: 2px solid var(--panel-line); }
  .facts-row .amount { width: 60px; text-align: right; }
  .facts-row .dv { width: 30px; text-align: right; }
  .facts-row .name { flex: 1; }
  .blend { font-weight: 700; }
  .sub .name { padding-left: 8px; }
  .facts-note { margin-top: 2px; }
  .facts-warning { margin-top: 2px; font-weight: 700; }
</style>
</head>
<body>
<main class="canvas">
  <section class="label">
    <div class="storm-backdrop" role="img" aria-label="Electric lightning storm backdrop in white and blue"></div>

    <div class="brand">
      <div class="brand-name">VYK</div>
      <div class="brand-tagline">Vigor, Yield &amp; Kinetics</div>
    </div>

    <div class="content-box">
      <div class="content-type">DIETARY SUPPLEMENT</div>
      <div class="content-count">60 CAPSULES</div>
    </div>

    <div class="facts-panel">
      <div class="facts-title">Supplement Facts</div>
      <div class="facts-row"><span class="name">Serving Size: 2 Capsules</span></div>
      <div class="facts-row heavy"><span class="name">Servings Per Container: 30</span></div>
      <div class="facts-row"><span class="name blend">Amount Per Serving</span><span class="dv">% Daily Value</span></div>
      <div class="facts-row"><span class="name">Niacin (as niacinamide)</span><span class="amount">10 mg</span><span class="dv">63%</span></div>
      <div class="facts-row"><span class="name">Vitamin B6 (as pyridoxine)</span><span class="amount">4 mg</span><span class="dv">235%</span></div>
      <div class="facts-row"><span class="name">Chromium (as picolinate)</span><span class="amount">200 mcg</span><span class="dv">571%</span></div>
      <div class="facts-row blend"><span class="name">Proprietary Calm Blend</span><span class="amount">450 mg</span><span class="dv">*</span></div>
      <div class="facts-row sub"><span class="name">Ashwagandha Root Extract</span><span class="dv">*</span></div>
      <div class="facts-row sub"><span class="name">Acetyl L-Carnitine HCl</span><span class="dv">*</span></div>
      <div class="facts-row sub"><span class="name">L-Theanine</span><span class="dv">*</span></div>
      <div class="facts-row blend"><span class="name">Proprietary Appetite Blend</span><span class="amount">400 mg</span><span class="dv">*</span></div>
      <div class="facts-row sub"><span class="name">Glucomannan Root Powder</span><span class="dv">*</span></div>
      <div class="facts-row sub"><span class="name">Garcinia Fruit Extract</span><span class="dv">*</span></div>
      <div class="facts-row sub"><span class="name">Cayenne Pepper Extract</span><span class="dv">*</span></div>
      <div class="facts-row blend"><span class="name">Proprietary Performance Blend</span><span class="amount">500 mg</span><span class="dv">*</span></div>
      <div class="facts-row sub"><span class="name">Green Tea Extract</span><span class="dv">*</span></div>
      <div class="facts-row sub"><span class="name">Theobromine</span><span class="dv">*</span></div>
      <div class="facts-row sub heavy"><span class="name">Green Coffee Bean Extract</span><span class="dv">*</span></div>
      <div class="facts-note">* Daily Value not established.</div>
      <div class="facts-note">Other Ingredients: Rice Flour, Gelatin Capsule.</div>
      <div class="facts-warning">Warning: Contains 215 mg of caffeine per serving.</div>
    </div>
  </section>
</main>
</body>
</html>
```